Business Card Design Project

Volleyball Club specializing in college prep training for athletes ranging in age from 5-18, for both indoor and beach volleyball.

Industry/Entity Type

Business

Contact Information for Business Card

Corinne Haldane
Summit VBC Club Director
corinnehaldane@summitvbc.example
P:555-204-7318
C:555-672-1045
F:555-819-3067
Web:summitvbc.example

Summit Volleyball Club Inc.
4721 Larkhaven Ave #206
Winnetka CA 90000

```html
<!DOCTYPE html>
<html lang="en">
<head>
<meta charset="utf-8">
<title>Summit VBC – Business Card</title>
<link rel="stylesheet" href="https://fonts.googleapis.com/css2?family=Cinzel:wght@600&family=Questrial&display=swap">
<style>
  :root {
    --page-bg: #ecebef;
    --card-top: #f1f0f6;
    --card-bottom: #d9d7e4;
    --brand-blue: #2c4b9e;
    --ink: #2b2b33;
    --rule: #5a5a66;
  }
  * { box-sizing: border-box; margin: 0; padding: 0; }
  html, body {
    width: 1200px; height: 800px; overflow: hidden;
    background: var(--page-bg);
  }
  .canvas {
    position: relative; width: 1200px; height: 800px;
    display: flex; align-items: center; justify-content: center;
  }
  .card {
    position: relative; width: 900px; height: 514px;
    background: radial-gradient(ellipse at 50% 35%, var(--card-top) 0%, var(--card-bottom) 100%);
    box-shadow: 0 10px 30px rgba(0,0,0,.18);
    overflow: hidden;
  }
  .brand-name {
    position: absolute; top: 78px; left: 0; right: 0;
    text-align: center; white-space: nowrap;
    font-family: "Cinzel", serif; font-weight: 600;
    font-size: 52px; letter-spacing: 3px;
    color: var(--brand-blue);
  }
  .player-figure {
    position: absolute;
    background: radial-gradient(ellipse at center, rgba(143,142,152,.75) 0%, rgba(143,142,152,.35) 55%, rgba(143,142,152,0) 75%);
  }
  .player-figure--left { left: 40px; top: 270px; width: 200px; height: 230px; }
  .player-figure--right { right: 40px; top: 120px; width: 230px; height: 240px; }
  .identity {
    position: absolute; top: 190px; left: 0; right: 0; text-align: center;
  }
  .identity__name {
    font-family: "Cinzel", serif; font-weight: 600; white-space: nowrap;
    font-size: 44px; color: var(--brand-blue); letter-spacing: 1px;
  }
  .identity__title {
    font-family: "Questrial", sans-serif; font-size: 22px;
    color: var(--ink); letter-spacing: 1.5px; margin-top: 2px;
  }
  .identity__rule {
    width: 190px; height: 2px; background: var(--rule);
    margin: 8px auto 0;
  }
  .contacts {
    position: absolute; top: 330px; left: 50%; transform: translateX(-50%);
    font-family: "Questrial", sans-serif; font-size: 21px;
    color: var(--ink); letter-spacing: 1.2px;
    white-space: nowrap;
  }
  .contacts__email { margin-bottom: 8px; }
  .contacts__columns { display: flex; gap: 48px; }
  .contacts__column { flex: none; }
  .contact-line { display: flex; align-items: center; gap: 14px; height: 34px; white-space: nowrap; }
  .contact-line svg { width: 20px; height: 20px; fill: var(--ink); flex: none; }
</style>
</head>
<body>
<div class="canvas">
  <div class="card">
    <div class="player-figure player-figure--left" role="img" aria-label="Silhouette of a volleyball player setting the ball"></div>
    <div class="player-figure player-figure--right" role="img" aria-label="Silhouette of a volleyball player jumping to spike"></div>

    <div class="brand-name">Summit Volleyball</div>

    <div class="identity">
      <div class="identity__name">Corinne Haldane</div>
      <div class="identity__title">Summit VBC Club Director</div>
      <div class="identity__rule"></div>
    </div>

    <div class="contacts">
      <div class="contact-line contacts__email">
        <svg viewBox="0 0 20 20" aria-hidden="true"><path d="M1 4h18v12H1z M2.5 5.5 10 11l7.5-5.5" fill="none" stroke="#2b2b33" stroke-width="1.6"/></svg>
        <span>corinnehaldane@summitvbc.example</span>
      </div>
      <div class="contacts__columns">
        <div class="contacts__column">
          <div class="contact-line">
            <svg viewBox="0 0 20 20" aria-hidden="true"><path d="M4 1.5l3 .5 1.5 4-2 1.5c1 2.5 3 4.5 5.5 5.5l1.5-2 4 1.5.5 3c-.5 1.5-2 2.5-3.5 2.5C8 18 2 12 2 5c0-1.5 1-3 2-3.5z"/></svg>
            <span>555-204-7318</span>
          </div>
          <div class="contact-line">
            <svg viewBox="0 0 20 20" aria-hidden="true"><path d="M6 1h8a1.5 1.5 0 0 1 1.5 1.5v15A1.5 1.5 0 0 1 14 19H6a1.5 1.5 0 0 1-1.5-1.5v-15A1.5 1.5 0 0 1 6 1zm0 2v12h8V3zm4 13a1 1 0 1 0 0 2 1 1 0 0 0 0-2z"/></svg>
            <span>555-672-1045</span>
          </div>
        </div>
        <div class="contacts__column">
          <div class="contact-line">
            <svg viewBox="0 0 20 20" aria-hidden="true"><path d="M5 1h10v5H5z M2 7h16v8h-3v4H5v-4H2z M7 13v4h6v-4z"/></svg>
            <span>555-819-3067</span>
          </div>
          <div class="contact-line">
            <svg viewBox="0 0 20 20" aria-hidden="true"><circle cx="10" cy="10" r="8.5" fill="none" stroke="#2b2b33" stroke-width="1.6"/><path d="M6 5c2 1 1 3 3 3s1 3 3 3-1 4-2 5M13 3c0 2 2 3 4 3"/></svg>
            <span>summitvbc.example</span>
          </div>
        </div>
      </div>
    </div>
  </div>
</div>
</body>
</html>
```